Packaging for a new tea company

Hi guys we need a new packaging design for a tea company we are starting

Our competitors are leafara, zo ren tea

I have uploaded pictures of our competitors for you to see the sample
The label need to be catchy

Our brand is called #PlumVexaTea
We need two packaging designs one for Day Tea and one for calmora

Detox - slim - cleanse

Also needs to says 14 Day Orvalin

Target Market(s)

Young people

Industry/Entity Type

It Company

Colors
000000

Requirements
Must have
• #plumvexatea
Nice to have
• Herbal tea supplement 50gram
• Max label size 13.5cm x 16.5 cm
• Personally I like the paper brown bag as it looks like a higher quality and as the label is a sticker I think this would make the product look a lot better
Should not have
• Nothing

```html
<!DOCTYPE html>
<html lang="en">
<head>
<meta charset="utf-8">
<title>Plum Vexa Tea – Day & Night Labels</title>
<link rel="stylesheet" href="https://fonts.googleapis.com/css2?family=Poppins:wght@400;600;700&family=Arimo:wght@400;700&display=swap">
<style>
  :root {
    --page: #ffffff;
    --divider: #9fd8f2;
    --orange: #f59a22;
    --orange-panel: #f7931e;
    --sun-center: #fcd24e;
    --sun-edge: #f09a1c;
    --leaf-soft: rgba(169,207,60,.55);
    --leaf-clear: rgba(169,207,60,0);
    --tag-green: #8dc63f;
    --ink-dark: #2a2016;
    --navy-center: #23489a;
    --navy-edge: #0a1747;
    --sky-blue: #29abe2;
    --band-blue: #1b3fa6;
    --flower-soft: rgba(58,79,142,.6);
    --flower-clear: rgba(58,79,142,0);
    --maroon: #7a1a12;
    --seal-gold: #f6b21b;
    --seal-silver: #b9bcc2;
    --cream: #fbe39a;
    --white: #ffffff;
  }
  * { box-sizing: border-box; margin: 0; padding: 0; }
  html, body { width: 1200px; height: 409px; overflow: hidden; background: var(--page); }
  .canvas { position: relative; width: 1200px; height: 409px; font-family: "Poppins", sans-serif; }
  .divider { position: absolute; left: 600px; top: 25px; width: 1px; height: 359px; background: var(--divider); }

  .label { position: absolute; top: 64px; width: 214px; height: 261px; border-radius: 8px; overflow: hidden; }
  .label > * { position: absolute; }
  .label--day-a { left: 62px; background: var(--orange); }
  .label--night-a { left: 326px; }
  .label--day-b { left: 660px; background: radial-gradient(circle at 50% 45%, var(--sun-center) 0%, var(--sun-edge) 85%); }
  .label--night-b { left: 924px; }
  .label--night-a, .label--night-b { background: radial-gradient(ellipse at 50% 38%, var(--navy-center) 0%, var(--navy-edge) 80%); }

  .inner-panel { left: 22px; top: 16px; width: 170px; height: 212px; background: var(--orange-panel); box-shadow: 0 1px 4px rgba(120,60,0,.35); }

  .brand-small { width: 100%; text-align: center; font-weight: 700; font-size: 16px; line-height: 1; }
  .brand-large { width: 100%; text-align: center; font-weight: 700; font-size: 32px; line-height: 1; letter-spacing: -0.3px; white-space: nowrap; }
  .ink-dark { color: var(--ink-dark); }
  .ink-light { color: var(--white); }

  .variant-box { left: 50%; transform: translateX(-50%); padding: 1px 8px; font-weight: 600; font-size: 10px; letter-spacing: 1px; color: var(--ink-dark); background: var(--cream); border: 2px solid var(--ink-dark); outline: 1px solid var(--cream); white-space: nowrap; }
  .variant-night { width: 100%; text-align: center; font-family: "Arimo", sans-serif; font-size: 11px; letter-spacing: 3px; color: var(--white); }

  .claims { width: 100%; text-align: center; font-family: "Arimo", sans-serif; font-size: 10.5px; }
  .claims--band { height: 14px; line-height: 14px; font-weight: 700; font-size: 9.5px; letter-spacing: .6px; }
  .band-cream { background: linear-gradient(90deg, rgba(251,227,154,.3), var(--cream) 20%, var(--cream) 80%, rgba(251,227,154,.3)); }
  .band-blue { background: linear-gradient(90deg, rgba(27,63,166,.3), var(--band-blue) 20%, var(--band-blue) 80%, rgba(27,63,166,.3)); }
  .weight { width: 100%; text-align: center; font-family: "Arimo", sans-serif; font-size: 7.5px; }

  .program-tag { right: 0; display: flex; flex-direction: column; align-items: center; justify-content: center; line-height: 1; }
  .program-tag .days { font-size: 12px; }
  .program-tag .name { font-size: 6.5px; letter-spacing: .4px; }

  .seal { border-radius: 50%; }
  .seal--gold { background: radial-gradient(circle, var(--seal-gold) 55%, #d48f0a 56%, var(--seal-gold) 62%); }
  .seal--silver { background: radial-gradient(circle, #8d9096 50%, var(--seal-silver) 52%, #6f7278 64%); }

  .decoration-leaves { background: radial-gradient(ellipse at 25% 100%, var(--leaf-soft) 0%, var(--leaf-clear) 70%); }
  .decoration-flowers { background: radial-gradient(ellipse at 50% 100%, var(--flower-soft) 0%, var(--flower-clear) 75%); }
</style>
</head>
<body>
<div class="canvas">

  <section class="label label--day-a" aria-label="Plum Vexa Tea Day Tea label, concept A">
    <div class="inner-panel"></div>
    <div class="decoration-leaves" role="img" aria-label="Green leafy vine decoration along the bottom" style="left:0;top:160px;width:214px;height:101px;"></div>
    <div class="seal seal--gold" style="left:33px;top:30px;width:42px;height:42px;"></div>
    <div class="program-tag" style="top:55px;width:47px;height:28px;background:var(--tag-green);color:var(--ink-dark);">
      <span class="days">14 <small style="font-size:6px">DAY</small></span><span class="name">ORVALIN</span>
    </div>
    <div class="brand-small ink-dark" style="top:90px;">Plum</div>
    <div class="brand-large ink-dark" style="top:111px;">Vexa Tea</div>
    <div class="variant-box" style="top:153px;">DAY TEA</div>
    <div class="claims ink-dark" style="top:186px;">DETOX - SLIM - CLEANSE</div>
    <div class="weight ink-dark" style="top:226px;">50gram</div>
  </section>

  <section class="label label--night-a" aria-label="Plum Vexa Tea Night Tea label, concept A">
    <div class="decoration-flowers" role="img" aria-label="Dark blue flower silhouettes along the bottom" style="left:0;top:150px;width:214px;height:111px;"></div>
    <div class="seal seal--silver" style="left:34px;top:56px;width:40px;height:40px;"></div>
    <div class="program-tag" style="top:59px;width:76px;height:27px;background:var(--sky-blue);color:var(--navy-edge);">
      <span class="days">14 <small style="font-size:6px">DAY</small></span><span class="name">ORVALIN</span>
    </div>
    <div class="brand-small ink-light" style="top:84px;">Plum</div>
    <div class="brand-large ink-light" style="top:103px;">Vexa Tea</div>
    <div class="variant-night" style="top:146px;">NIGHT TEA</div>
    <svg style="left:160px;top:155px;" width="14" height="14" viewBox="0 0 14 14" aria-hidden="true"><path d="M9 1a6 6 0 1 0 4 10A5 5 0 0 1 9 1z" fill="var(--white)"/></svg>
    <div class="claims ink-light" style="top:202px;">DETOX - SLIM - CLEANSE</div>
    <div class="weight ink-light" style="top:222px;">50gram</div>
  </section>

  <div class="divider"></div>

  <section class="label label--day-b" aria-label="Plum Vexa Tea Day Tea label, concept B">
    <div class="decoration-leaves" role="img" aria-label="Light green leafy vine decoration rising from the bottom left" style="left:0;top:90px;width:160px;height:171px;"></div>
    <svg style="left:78px;top:40px;" width="64" height="54" viewBox="0 0 64 54" aria-hidden="true"><path d="M4 18 L60 6 L60 34 L4 46 Z" fill="var(--maroon)"/></svg>
    <div class="program-tag" style="top:66px;width:68px;height:34px;background:var(--tag-green);color:var(--white);">
      <span class="days" style="font-size:16px;">14 <small style="font-size:7px">DAY</small></span><span class="name" style="font-size:8px;color:var(--ink-dark);">ORVALIN</span>
    </div>
    <div class="brand-small ink-dark" style="top:92px;left:-52px;font-size:17px;">Plum</div>
    <div class="brand-large ink-dark" style="top:110px;">Vexa Tea</div>
    <div class="variant-box" style="top:153px;">DAY TEA</div>
    <div class="claims claims--band band-cream ink-dark" style="top:185px;">DETOX - SLIM - CLEANSE</div>
    <div class="weight ink-dark" style="top:226px;">50gram</div>
  </section>

  <section class="label label--night-b" aria-label="Plum Vexa Tea Night Tea label, concept B">
    <div class="decoration-flowers" role="img" aria-label="Dark blue flower silhouettes along the bottom" style="left:0;top:150px;width:214px;height:111px;"></div>
    <svg style="left:84px;top:32px;" width="62" height="54" viewBox="0 0 62 54" aria-hidden="true"><path d="M4 22 L58 8 L58 34 L4 48 Z" fill="var(--sky-blue)"/></svg>
    <div class="program-tag" style="top:74px;width:73px;height:28px;background:var(--white);color:var(--navy-edge);">
      <span class="days">14 <small style="font-size:6px">DAY</small></span><span class="name">ORVALIN</span>
    </div>
    <div class="brand-small ink-light" style="top:86px;left:-52px;font-size:17px;">Plum</div>
    <div class="brand-large ink-light" style="top:106px;">Vexa Tea</div>
    <div class="variant-night" style="top:146px;">NIGHT TEA</div>
    <svg style="left:168px;top:154px;" width="14" height="14" viewBox="0 0 14 14" aria-hidden="true"><path d="M9 1a6 6 0 1 0 4 10A5 5 0 0 1 9 1z" fill="var(--white)"/></svg>
    <div class="claims claims--band band-blue ink-light" style="top:185px;">DETOX - SLIM - CLEANSE</div>
    <div class="weight ink-light" style="top:205px;">50gram</div>
  </section>

</div>
</body>
</html>
```